Sports coaching website.

Hi there web designers,

We need a modern fully functional website to set us apart from our competition. The website will be information based with pictures and videos provided by us. The website must include members log in where they can pay for sessions directly online and subscribe to direct debit.

Target Market(s)

parents/teachers/schools/community/children.

Number of Pages Required

5+ page

Font styles to use
Sans Serif

Colors
acd037
3176b5
ffffff
000000
919191
f37122

Requirements
Must have
• Pictures, be modern, fully functional, must be clear, bold, e-basket, log-in.

```html
<!DOCTYPE html>
<html lang="en">
<head>
<meta charset="utf-8">
<title>Prime Play Sports</title>
<link rel="stylesheet" href="https://fonts.googleapis.com/css2?family=Merriweather:wght@300;400;700&display=swap">
<style>
:root{
  --black:#000000;
  --red:#7a0000;
  --white:#ffffff;
  --green:#a3c52d;
  --orange:#f37122;
  --blue:#3a78b8;
  --grey:#919191;
  --dark-grey:#555555;
  --footer:#333333;
  --lime:#d6ef3a;
}
*{margin:0;padding:0;box-sizing:border-box}
html,body{width:807px;height:1200px;overflow:hidden;background:var(--white)}
body{position:relative;font-family:'Merriweather',serif;color:var(--dark-grey)}
.abs{position:absolute}

.top-bar{left:0;top:0;width:807px;height:39px;background:var(--black)}
.red-band{left:0;top:39px;width:807px;height:23px;background:var(--red)}
.account-links{left:254px;top:16px;display:flex;gap:10px;font-size:6px;color:var(--white);text-transform:uppercase}
.social-links{left:459px;top:16px;display:flex;gap:6px}
.social-links span{width:7px;height:7px;border-radius:50%;background:var(--white)}
.brand{left:356px;top:4px;width:94px;height:72px;background:var(--black);display:flex;align-items:center;justify-content:center;gap:5px;color:var(--white);font-weight:700;font-size:9px;text-transform:uppercase;text-align:center;line-height:1.2}
.brand-dot{width:10px;height:10px;border-radius:50%;background:var(--orange);flex:none}

.main-nav{left:0;top:62px;width:807px;height:46px}
.main-nav a{position:absolute;top:25px;transform:translateX(-50%);font-size:8.4px;font-weight:700;color:var(--black);text-decoration:none;white-space:nowrap;letter-spacing:.2px}

.photo{background:linear-gradient(160deg,#b59a6e,#8a6b48 55%,#c9a979)}
.hero-photo{left:0;top:108px;width:807px;height:352px;background:linear-gradient(180deg,#9fa9a8 0%,#6d6055 35%,#b48b55 70%,#c9a775 100%)}

.event-card{left:111px;top:319px;width:360px;height:156px;background:var(--green);color:var(--white);padding:24px 26px}
.event-card h2{font-size:14px;font-weight:400;letter-spacing:.3px}
.event-date{font-size:5.5px;margin-top:3px}
.event-text{font-size:7px;line-height:1.35;margin-top:8px;width:300px}
.btn{display:inline-block;border:1px solid var(--white);color:var(--white);font-size:7.5px;padding:7px 16px;margin-top:11px;text-transform:uppercase}
.dots{display:flex;gap:5px}
.dots span{width:6px;height:6px;border-radius:50%;background:rgba(255,255,255,.6)}
.dots span:first-child{background:var(--white)}
.event-card .dots{position:absolute;left:27px;bottom:20px}

.about-card{left:472px;top:287px;width:224px;height:173px;background:var(--orange);color:var(--white);padding:21px 21px}
.about-card h2{font-size:20px;font-weight:400}
.about-card p{font-size:7.6px;line-height:1.3;margin-top:14px;width:180px}

.video-photo{left:111px;top:475px;width:360px;height:223px;background:linear-gradient(170deg,#c49b6a,#a27a50 60%,#c8a57a)}
.play-icon{left:268px;top:553px}
.cricket-photo{left:472px;top:460px;width:224px;height:238px;background:linear-gradient(175deg,#9da0a5 0%,#b89468 35%,#c7a272 100%)}

.feature{top:724px;width:160px;text-align:center;transform:translateX(-50%)}
.feature svg{display:block;margin:0 auto;height:44px}
.feature h3{font-size:8px;font-weight:400;color:#555;margin-top:11px;text-transform:uppercase}
.feature p{font-size:6.6px;line-height:1.3;color:var(--grey);margin-top:6px}

.testimonials{left:0;top:873px;width:807px;height:281px;background:linear-gradient(180deg,#3d7cbd,#3470ae);color:var(--white);text-align:center}
.testimonials h2{position:absolute;left:0;right:0;top:64px;font-size:21px;font-weight:400}
.quote-text{position:absolute;left:198px;width:412px;top:98px;font-size:10.4px;font-weight:300;line-height:1.6}
.quote-mark{position:absolute;top:100px;font-size:34px;font-weight:700;line-height:1}
.author-photo{position:absolute;left:327px;top:168px;width:46px;height:46px;border-radius:50%;border:2px solid var(--white);background:linear-gradient(160deg,#4d8f4a,#b8c4cf)}
.author{position:absolute;left:387px;top:175px;text-align:left}
.author strong{display:block;font-size:13px;font-weight:400;color:var(--lime)}
.author span{font-size:6.4px}
.testimonials .dots{position:absolute;left:389px;top:232px}

.site-footer{left:0;top:1154px;width:807px;height:46px;background:var(--footer);color:var(--white);font-size:6.4px;text-transform:uppercase}
.site-footer .copy{position:absolute;left:112px;top:21px}
.site-footer .legal{position:absolute;right:111px;top:21px}
</style>
</head>
<body>
<header>
  <div class="abs top-bar"></div>
  <div class="abs red-band"></div>
  <nav class="abs account-links"><span>Sign in</span><span>Sign up</span><span>Contact</span></nav>
  <div class="abs social-links"><span></span><span></span><span></span><span></span><span></span><span></span></div>
  <div class="abs brand"><span class="brand-dot"></span><span>Prime Play<br>Sports</span></div>
  <nav class="abs main-nav">
    <a style="left:140px">HOME</a>
    <a style="left:210px">ABOUT PPS</a>
    <a style="left:286px">SCHOOLS</a>
    <a style="left:361px">SESSIONS</a>
    <a style="left:439px">WORKSHOPS</a>
    <a style="left:547px">CHARITY/COMMUNITY</a>
    <a style="left:649px">CONTACT</a>
  </nav>
</header>

<main>
  <div class="abs hero-photo" role="img" aria-label="Coaches and children in a sports hall holding up footballs"></div>

  <section class="abs event-card">
    <h2>FOOTBALL LEAGUE 3 ON 3</h2>
    <div class="event-date">AUGUST 23, 2016</div>
    <p class="event-text">Neque porro quisquam est, qui dolorem ipsum quia dolor sit qui dolorem quae adipisci velit, sed quia non numquam eius modi tempora inc sed quia non num dolore magnam aliquam quaerat voluptatem.</p>
    <span class="btn">Book now!</span>
    <div class="dots"><span></span><span></span><span></span><span></span></div>
  </section>

  <section class="abs about-card">
    <h2>WHO ARE WE?</h2>
    <p>Excepturi sint occaecati cupiditate non provident, similiue sunt in culp qui officia deserunt mollitia animi, id est laborum et dolorum fuga. Et harum quidem rerum facilis est et expedita distinctio.</p>
    <span class="btn">More</span>
  </section>

  <div class="abs video-photo" role="img" aria-label="Children sitting on a sports hall floor holding up balls"></div>
  <svg class="abs play-icon" width="54" height="54" viewBox="0 0 54 54" aria-hidden="true">
    <circle cx="27" cy="27" r="24" fill="none" stroke="#fff" stroke-width="4"/>
    <path d="M21 15 L38 27 L21 39 Z" fill="#fff"/>
  </svg>
  <div class="abs cricket-photo" role="img" aria-label="Child batting at cricket stumps while others play in a sports hall"></div>

  <section>
    <div class="abs feature" style="left:207px">
      <svg viewBox="0 0 60 44" width="60" aria-hidden="true">
        <path d="M8 30 L30 16 L44 18 L46 30 L30 38 Z" fill="#888"/>
        <circle cx="18" cy="33" r="9" fill="#888"/>
        <path d="M44 18 Q46 6 54 2" fill="none" stroke="#888" stroke-width="1.5"/>
      </svg>
      <h3>Qualified coaches</h3>
      <p>Lorem ipsum dolor sit amet, consectetur adipiscing elit, sed do eiusmod tempor incidunt ut labore et doloe magna aliqua.</p>
    </div>
    <div class="abs feature" style="left:399px">
      <svg viewBox="0 0 44 44" width="44" aria-hidden="true">
        <rect x="4" y="20" width="8" height="20" fill="#888"/>
        <path d="M14 20 L22 6 Q27 4 26 12 L25 18 L36 18 Q40 19 39 24 L36 38 Q35 40 32 40 L14 40 Z" fill="#888"/>
      </svg>
      <h3>Approved by parents</h3>
      <p>Duis aute irure dolor in reprehenderit in voluptate velit esse cillum dolore eu fugiat nulla pariatur. Excepteur sint .</p>
    </div>
    <div class="abs feature" style="left:596px">
      <svg viewBox="0 0 44 44" width="44" aria-hidden="true">
        <g fill="none" stroke="#888" stroke-width="2.4">
          <circle cx="22" cy="22" r="18"/>
          <path d="M9 9 Q22 20 35 35"/>
          <path d="M35 9 L9 35"/>
          <path d="M4 20 Q16 18 22 6"/>
          <path d="M22 38 Q28 26 40 24"/>
        </g>
      </svg>
      <h3>Modern sports equipment</h3>
      <p>Lorem ipsum dolor sit amet, consectetur adipiscing elit, sed do eiusmod tempor incidunt ut labore et doloe magna aliqua.</p>
    </div>
  </section>

  <section class="abs testimonials" role="img" aria-label="Blue-tinted photo of children playing, behind the testimonials">
    <h2>OUR TESTIMONIALS</h2>
    <span class="quote-mark" style="left:161px">“</span>
    <p class="quote-text">Neque porro quisquam est, qui dolorem ipsum quia dolor sit amet, consectetur, adipisci velit, sed quia non numquam eius modi tempora incidunt ut labore et dolore magnam aliquam quaerat voluptatem.</p>
    <span class="quote-mark" style="left:638px">”</span>
    <div class="author-photo" role="img" aria-label="Portrait of the reviewer"></div>
    <div class="author"><strong>DANIEL MOSS</strong><span>Eastfield College Teacher</span></div>
    <div class="dots"><span></span><span></span><span></span></div>
  </section>
</main>

<footer class="abs site-footer">
  <span class="copy">© Copyright 2016 &nbsp;Prime Play Sports</span>
  <span class="legal">Privacy | Terms</span>
</footer>
</body>
</html>
```